Design a label for a dog shampoo names furbloom, the sell point of this series of shampoo is “just like wash your dogs with milk, not harm for your hand ”, the style could be gentle or professional or even amazing.

Use only 2 colors in the design job, the color of our logo could be changed, it depends on your whole page. Please design in CDR or ai.

update:
Pls do more change with the fonts when you design the front page, including title and details. Try more styles of fonts. Addition, this design will be printed on the bottle, no a label stick on it.
Updates

Do not put a real dog or animal on the page, Pay more attention to the types of fonts

Reason: Expect for more design idea.

Target Market(s)

people 20-30 years old who have dogs and cats at home

Industry/Entity Type

It Professional

Requirements
Nice to have
• It would be nice if you add some detail words in the design of the right side.

```html
<!DOCTYPE html>
<html lang="en">
<head>
<meta charset="utf-8">
<title>furbloom — super conditioning nutrient shampoo</title>
<link href="https://fonts.googleapis.com/css2?family=Fredoka:wght@600&family=Quicksand:wght@400&display=swap" rel="stylesheet">
<style>
  :root {
    --ink-blue: #035fa3;
    --milk-blue: #b8d8ef;
    --paper: #ffffff;
  }
  html, body {
    margin: 0;
    padding: 0;
    width: 1200px;
    height: 2297px;
    overflow: hidden;
    background: var(--paper);
  }
  .label {
    position: relative;
    width: 1200px;
    height: 2297px;
    background: var(--paper);
  }
  .brand-name {
    position: absolute;
    left: 90px;
    top: 560px;
    width: 1020px;
    height: 380px;
  }
  .brand-name text {
    font-family: "Fredoka", sans-serif;
    font-weight: 600;
    fill: var(--ink-blue);
  }
  .claims {
    position: absolute;
    left: 130px;
    top: 1050px;
    width: 400px;
    margin: 0;
    padding: 0;
    list-style: none;
    text-align: right;
    font-family: "Fredoka", sans-serif;
    font-weight: 600;
    font-size: 52px;
    line-height: 98px;
    letter-spacing: 5px;
    color: var(--milk-blue);
    transform: skewX(-6deg);
  }
  .claims .volume { font-size: 48px; }
  .product-band {
    position: absolute;
    left: 100px;
    top: 1440px;
    width: 1000px;
    height: 340px;
  }
  .product-band svg {
    position: absolute;
    inset: 0;
  }
  .product-band .cloud { fill: var(--milk-blue); }
  .product-type {
    position: absolute;
    left: 0;
    right: 0;
    top: 78px;
    margin: 0;
    text-align: center;
    font-family: "Quicksand", sans-serif;
    font-weight: 400;
    font-size: 70px;
    line-height: 100px;
    letter-spacing: 17px;
    color: var(--paper);
    transform: skewX(-12deg);
  }
</style>
</head>
<body>
<main class="label">
  <svg class="brand-name" viewBox="0 0 1020 380" aria-label="furbloom">
    <text x="510" y="300" text-anchor="middle" font-size="300" textLength="1000" lengthAdjust="spacingAndGlyphs">furbloom</text>
  </svg>

  <ul class="claims">
    <li>moisture rich</li>
    <li>smooth &amp; silky</li>
    <li class="volume">100ml</li>
  </ul>

  <section class="product-band">
    <svg viewBox="0 0 1000 340" preserveAspectRatio="none" aria-hidden="true">
      <path class="cloud" d="M40 40 Q120 5 230 22 Q330 0 440 18 Q560 2 670 20 Q790 0 900 14 Q985 10 990 70 Q1000 130 985 170 Q1000 230 990 290 Q980 335 900 325 Q800 340 690 326 Q580 340 460 325 Q350 340 240 326 Q130 340 60 322 Q5 310 12 250 Q0 190 14 150 Q0 90 40 40 Z"/>
    </svg>
    <h1 class="product-type">super conditioning<br>nutrient shampoo</h1>
  </section>
</main>
</body>
</html>
```